rural business needs a sign design

We need a signage design for a rural business in south Australia ,called 'Tarlewyn ' would like the signage to be in the Celtic style script we also would like some sort of Celtic symbol to go with it as a graphic eg scotch thistle ,Celtic cross etc. we would like the background to be either dark blue ,navy or black

```html
<!DOCTYPE html>
<html lang="en">
<head>
<meta charset="utf-8">
<title>Tarlewyn sign</title>
<link rel="stylesheet" href="https://fonts.googleapis.com/css2?family=Uncial+Antiqua&display=swap">
<style>
  :root {
    --navy: #0d0442;
    --gold: #e0921e;
    --ornament-grey: #4a4668;
    --ornament-soft: #2a2358;
  }
  html, body {
    margin: 0;
    padding: 0;
    overflow: hidden;
    background: var(--navy);
  }
  .sign {
    position: relative;
    width: 1200px;
    height: 362px;
    background: var(--navy);
    overflow: hidden;
  }
  .ornament {
    position: absolute;
    display: block;
  }
  .ornament--cross {
    left: 8px;
    top: 0;
    width: 330px;
    height: 362px;
  }
  .ornament--knot {
    left: 985px;
    top: 14px;
    width: 212px;
    height: 205px;
  }
  .sign__name {
    position: absolute;
    left: 0;
    right: 0;
    top: 30px;
    margin: 0;
    text-align: center;
    font-family: "Uncial Antiqua", serif;
    font-weight: 400;
    font-size: 196px;
    line-height: 300px;
    color: var(--gold);
    letter-spacing: 2px;
  }
</style>
</head>
<body>
  <div class="sign">
    <svg class="ornament ornament--cross" viewBox="0 0 330 362" role="img" aria-label="Celtic cross with interlaced knotwork and ring">
      <defs>
        <radialGradient id="cross-tone" cx="50%" cy="45%" r="60%">
          <stop offset="0%" stop-color="var(--ornament-grey)"/>
          <stop offset="100%" stop-color="var(--ornament-soft)"/>
        </radialGradient>
      </defs>
      <rect x="0" y="0" width="330" height="362" rx="24" fill="url(#cross-tone)" opacity="0.7"/>
    </svg>

    <svg class="ornament ornament--knot" viewBox="0 0 212 205" role="img" aria-label="Celtic interlaced knot corner ornament">
      <rect x="0" y="0" width="212" height="205" rx="20" fill="var(--ornament-soft)" opacity="0.8"/>
    </svg>

    <h1 class="sign__name">Tarlewyn</h1>
  </div>
</body>
</html>
```